Trucking/service truck *Updated

Cards for a trucking company. Company transfers logs to saw mills. We are looking for something edgy, modern and fun. It's very limited when it comes to trucking business card choices. Plus the owner also runs an on-site service truck. He has 20+ years mechanic experience.
Colors are open. Favorites are orange & purple, but not must have. We really want to emphasize trust, dependability and knowledge with a bright, attention getter.
On card:
Hallowell & Hallowell
Dean Hallowell - Owner/Manager/Maintenance 903-512-4097
Marla Hallowell -Office Administration/Bookkeeping 903-627-1954
4718 Juniper Ln.
Cedar Bluff, Kansas 75392
903-659-3021 - Office
Updates
Just a thought. Do you think you can combine the Taurus and Pisces signs? And put in the corner, or on the back or anything really? Thanks! You all or doing fantastic!
Industry/Entity Type
Business
Colors
Designer to choose colors to be used in the design.
Look and feel
Each slider illustrates characteristics of the customer's brand and the style your logo design should communicate.

```html
<!DOCTYPE html>
<html lang="en">
<head>
<meta charset="UTF-8">
<title>Hallowell &amp; Hallowell — Business Cards</title>
<link rel="stylesheet" href="https://fonts.googleapis.com/css2?family=Oswald:wght@600&family=Open+Sans:wght@400;700&display=swap">
<style>
  :root {
    --page-bg: #e9e9e9;
    --card-front: #e4e4e4;
    --card-back: #ffffff;
    --brand-red: #e41e26;
    --brand-orange: #f07a14;
    --ink-dark: #2b2b2b;
    --ink-mid: #555555;
    --icon-blue: #2a4f8f;
  }
  * { box-sizing: border-box; margin: 0; padding: 0; }
  html, body { width: 1200px; height: 1200px; overflow: hidden; }
  body {
    background: var(--page-bg);
    font-family: "Open Sans", Arial, sans-serif;
    display: flex;
    flex-direction: column;
    align-items: center;
    justify-content: center;
    gap: 70px;
  }
  .card {
    position: relative;
    width: 700px;
    height: 400px;
    box-shadow: 0 6px 22px rgba(0,0,0,0.12);
    overflow: hidden;
  }

  /* Front */
  .card--front {
    background: var(--card-front);
    display: flex;
    align-items: center;
    justify-content: center;
    gap: 22px;
  }
  .front__mark {
    width: 46px;
    height: 46px;
    background: var(--brand-red);
  }
  .front__name {
    font-family: "Oswald", "Arial Narrow", sans-serif;
    font-weight: 600;
    font-size: 48px;
    line-height: 1;
    color: var(--brand-orange);
  }

  /* Back */
  .card--back { background: var(--card-back); }
  .back__brand {
    position: absolute;
    right: 36px; top: 36px;
    font-family: "Oswald", "Arial Narrow", sans-serif;
    font-weight: 600;
    font-size: 42px;
    line-height: 1.1;
    color: var(--brand-orange);
  }
  .back__people {
    position: absolute;
    left: 40px; top: 118px;
    width: 310px;
  }
  .person { margin-bottom: 18px; }
  .person__name { font-weight: 700; font-size: 23px; color: var(--ink-dark); line-height: 1.15; }
  .person__role { font-size: 17px; color: var(--ink-mid); line-height: 1.3; }
  .contact-line {
    display: flex; align-items: flex-start; gap: 8px;
    font-size: 17px; color: var(--ink-mid); line-height: 1.3;
  }
  .contact-line svg { flex: none; margin-top: 3px; }
  .back__divider {
    position: absolute;
    left: 368px; top: 130px;
    width: 3px; height: 180px;
    background: var(--brand-red);
  }
  .back__office {
    position: absolute;
    left: 398px; top: 190px;
  }
  .back__office .contact-line { margin-bottom: 14px; font-size: 19px; }
</style>
</head>
<body>

<section class="card card--front" aria-label="Card front">
  <div class="front__mark" aria-hidden="true"></div>
  <p class="front__name">Hallowell &amp; Hallowell</p>
</section>

<section class="card card--back" aria-label="Card back">
  <p class="back__brand">Hallowell &amp; Hallowell</p>

  <div class="back__people">
    <div class="person">
      <p class="person__name">Dean Hallowell</p>
      <p class="person__role">Owner/Manager/Maintenance</p>
      <p class="contact-line">
        <svg width="16" height="16" viewBox="0 0 16 16" aria-hidden="true"><circle cx="8" cy="8" r="8" fill="var(--icon-blue)"/><rect x="5.5" y="3.5" width="5" height="9" rx="1" fill="none" stroke="#fff" stroke-width="1.3"/></svg>
        903-512-4097
      </p>
    </div>
    <div class="person">
      <p class="person__name">Marla Hallowell</p>
      <p class="person__role">Office Administration/Bookkeeping</p>
      <p class="contact-line">
        <svg width="16" height="16" viewBox="0 0 16 16" aria-hidden="true"><circle cx="8" cy="8" r="8" fill="var(--icon-blue)"/><rect x="5.5" y="3.5" width="5" height="9" rx="1" fill="none" stroke="#fff" stroke-width="1.3"/></svg>
        903-627-1954
      </p>
    </div>
  </div>

  <div class="back__divider"></div>

  <div class="back__office">
    <p class="contact-line">
      <svg width="18" height="18" viewBox="0 0 16 16" aria-hidden="true"><circle cx="8" cy="8" r="8" fill="var(--icon-blue)"/><path d="M3.5 8 8 4l4.5 4H11v3.5H5V8z" fill="#fff"/></svg>
      <span>4718 Juniper Ln.<br>Cedar Bluff, Kansas 75392</span>
    </p>
    <p class="contact-line">
      <svg width="18" height="18" viewBox="0 0 16 16" aria-hidden="true"><circle cx="8" cy="8" r="8" fill="var(--icon-blue)"/><rect x="4" y="5" width="8" height="6" rx="1" fill="#fff"/><rect x="6" y="3.5" width="4" height="2" fill="#fff"/></svg>
      903-659-3021
    </p>
  </div>
</section>

</body>
</html>
```